Gardening and life coaching business card design

I need business cards for a new company in the heart of the Ozarks at the Lake of the Ozarks. Tallow Brook Harvest's mission is to teach the world to fish. We provide fresh local fish and produce using permaculture methods. We work with nature and the flow to create more harmony and less impact. We also coach others who are ready to make this transition. We specialize in microgreens and Aquaculture systems. I would like to make Tallow Brook Harvest come alive with green vines and purple flowers I wold like Tallow Brook Harvest to be in green and the rest of the lettering to be in purple. The feel of the card should be that of the Garden of Eden.

Industry/Entity Type

Life Coaching

Contact Information for Business Card

Tallow Brook Harvest
Owner/Operator Marisol Pettigrew
Contact Info:
(555) 214-9083
tallowbrookharvest.example
tallowbrookharvest is also on FB

```html
<!DOCTYPE html>
<html lang="en">
<head>
<meta charset="utf-8">
<title>Tallow Brook Harvest – Business Card</title>
<link rel="stylesheet" href="https://fonts.googleapis.com/css2?family=Source+Sans+3:wght@400;600&display=swap">
<style>
  :root {
    --page: #fdfdfd;
    --leaf: #55ae35;
    --stone: #e2e0df;
    --mist: #e3e2de;
    --plum: #7b1e5e;
  }
  html, body {
    margin: 0;
    padding: 0;
    width: 1200px;
    height: 846px;
    overflow: hidden;
    background: var(--page);
    font-family: "Source Sans 3", "Myriad Pro", Arial, sans-serif;
  }
  .sheet {
    position: relative;
    width: 1200px;
    height: 846px;
  }
  .card {
    position: absolute;
    top: 263px;
    width: 525px;
    height: 308px;
    box-sizing: border-box;
  }
  .card--front {
    left: 48px;
    background: var(--leaf);
    display: flex;
    align-items: center;
    justify-content: center;
  }
  .front-title {
    margin: 0;
    padding-bottom: 2px;
    color: var(--mist);
    font-size: 29px;
    font-weight: 600;
    letter-spacing: 0.1px;
  }
  .card--back {
    left: 626px;
    background: var(--stone);
    text-align: center;
  }
  .back-title {
    position: absolute;
    top: 112px;
    left: 0;
    right: 0;
    margin: 0;
    color: var(--leaf);
    font-size: 21px;
    font-weight: 600;
  }
  .holder-name {
    position: absolute;
    top: 141px;
    left: 0;
    right: 0;
    margin: 0;
    color: var(--plum);
    font-size: 16px;
    font-weight: 600;
  }
  .holder-role {
    position: absolute;
    top: 161px;
    left: 0;
    right: 0;
    margin: 0;
    color: var(--plum);
    font-size: 9.5px;
    letter-spacing: 0.3px;
  }
  .contact {
    position: absolute;
    top: 254px;
    left: 0;
    right: 0;
    margin: 0;
    color: var(--plum);
    font-size: 12.5px;
    line-height: 14px;
  }
  .contact-line { display: block; }
  .social-mark {
    display: inline-block;
    width: 8px;
    height: 8px;
    margin: 0 2px 0 6px;
    background: var(--plum);
    vertical-align: 0;
  }
  .footer-band {
    position: absolute;
    left: 0;
    bottom: 0;
    width: 100%;
    height: 18px;
    background: var(--leaf);
  }
</style>
</head>
<body>
  <main class="sheet">
    <section class="card card--front">
      <h1 class="front-title">Tallow Brook Harvest</h1>
    </section>
    <section class="card card--back">
      <h2 class="back-title">Tallow Brook Harvest</h2>
      <p class="holder-name">Marisol Pettigrew</p>
      <p class="holder-role">OWNER / OPERATOR</p>
      <p class="contact">
        <span class="contact-line">contact info: (555) 214-9083</span>
        <span class="contact-line">tallowbrookharvest.example<span class="social-mark"></span>tallowbrookharvest</span>
      </p>
      <div class="footer-band"></div>
    </section>
  </main>
</body>
</html>
```